Cedar Row Maintenance and Concierge Flyer

We need a flyer for cedar row maintenance and concierge service. We specialize in and provide residential maintenance and errand services to retired and semi retired persons living in the Lake Norman area. The services we include:
Lighting and plumbing repairs
Ceiling fan installation
Handicap accessories
Locks and security
Picture hanging
Hang blinds
Furniture arrangement / assembly
Pressure washing
Battery Jump start
and more...

Our Concierge services include:
Errand running
Grocery shopping
Wellness Checks
Dog Walk
Garbage Collection
and more...

We offer monthly service agreements and 24/7 access
Call text or e-mail for more information
704.555.0187
1cedarrowmaint@quillpostmail.com

The design should invoke a sense of trust and a customer service driven mission

Target Market(s)

Residential maintenance

Industry/Entity Type

Property Maintenance

Contact Information for Business Card

Derek Halvorsen
48176 Quimby Ferrel Rd.
Cornelius NC 28031
704.555.0187
with uploaded logo

Requirements
Nice to have
• Would like a postcard size flyer. Front and back
Should not have
• No pics of of people wearing hard hats or pics of blueprints. No pics of commercial or industrial maintenance.

```html
<!DOCTYPE html>
<html lang="en">
<head>
<meta charset="utf-8">
<title>Cedar Row Maintenance and Concierge Flyer</title>
<link href="https://fonts.googleapis.com/css2?family=Montserrat:wght@400;500;700&display=swap" rel="stylesheet">
<style>
  :root {
    --red: #d7212f;
    --dark-red: #b5121f;
    --ink: #3a3a3a;
    --grey: #8c8c8c;
    --light-grey: #bdbdbd;
    --star: #f4a21b;
    --white: #ffffff;
    --photo-blue: #6f7f95;
    --photo-warm: #c9a56a;
  }
  * { margin: 0; padding: 0; box-sizing: border-box; }
  html, body { width: 859px; height: 1200px; overflow: hidden; background: var(--white); }
  body { font-family: "Montserrat", Arial, sans-serif; color: var(--ink); }
  .flyer { position: relative; width: 859px; height: 1200px; overflow: hidden; background: var(--white); }

  .headline {
    position: absolute; left: 83px; top: 96px; width: 640px;
    color: var(--red); font-weight: 700; font-size: 29px; line-height: 35px;
  }
  .headline .stars { color: var(--star); font-size: 24px; letter-spacing: 1px; }

  .service-block { position: absolute; left: 83px; }
  .service-block.maintenance { top: 255px; }
  .service-block.concierge { top: 592px; }
  .service-block h2 { color: var(--red); font-size: 20px; font-weight: 700; margin-bottom: 4px; }
  .service-block ul { list-style: none; }
  .service-block li, .service-block .more { font-size: 19px; line-height: 28.5px; color: var(--ink); }
  .service-block li::before { content: "\2022"; margin-right: 7px; }

  .photo-ring { position: absolute; }
  .photo-ring.repair { left: 500px; top: 238px; }
  .photo-ring.errand { left: 500px; top: 528px; }

  .brand {
    position: absolute; left: 0; width: 859px; top: 870px;
    display: flex; justify-content: center; align-items: center; gap: 16px;
  }
  .brand .mark { width: 40px; height: 40px; border-radius: 50%; background: var(--red); }
  .brand .name { color: var(--grey); font-size: 24px; font-weight: 500; letter-spacing: 0.5px; }

  .footer-wave { position: absolute; left: 0; top: 990px; }
  .offer {
    position: absolute; left: 160px; top: 1050px; width: 245px;
    color: var(--white); font-weight: 700; font-size: 22px; line-height: 28px; text-align: center;
  }
  .divider { position: absolute; left: 398px; top: 1045px; width: 2px; height: 120px; background: rgba(255,255,255,0.7); }
  .contact { position: absolute; left: 410px; top: 1043px; width: 300px; text-align: center; color: var(--white); }
  .contact .prompt { font-size: 15px; line-height: 20px; }
  .contact .phone { font-size: 36px; font-weight: 700; margin-top: 6px; letter-spacing: 0.5px; }
  .contact .email { font-size: 14.5px; margin-top: 4px; }
</style>
</head>
<body>
<main class="flyer">
  <h1 class="headline">Providing 5 star services to Lake Norman residents with special attention to retired and semi retired citizens <span class="stars">★★★★★</span></h1>

  <section class="service-block maintenance">
    <h2>The services we include:</h2>
    <ul>
      <li>Lighting and plumbing repairs</li>
      <li>Ceiling fan installation</li>
      <li>Handicap accessories</li>
      <li>Locks and security</li>
      <li>Picture hanging</li>
      <li>Hang blinds</li>
      <li>Furniture arrangement / assembly</li>
      <li>Pressure washing</li>
      <li>Battery Jump start</li>
    </ul>
    <p class="more">and more...</p>
  </section>

  <section class="service-block concierge">
    <h2>Our Concierge services include:</h2>
    <ul>
      <li>Errand running</li>
      <li>Grocery shopping</li>
      <li>Wellness Checks</li>
      <li>Dog Walk</li>
      <li>Garbage Collection</li>
    </ul>
    <p class="more">and more...</p>
  </section>

  <svg class="photo-ring repair" width="300" height="290" viewBox="0 0 300 290">
    <defs>
      <linearGradient id="repairTone" x1="0" y1="0" x2="1" y2="1">
        <stop offset="0" stop-color="#b9b3a6"/>
        <stop offset="1" stop-color="var(--photo-blue)"/>
      </linearGradient>
    </defs>
    <circle cx="152" cy="145" r="142" fill="var(--red)"/>
    <circle cx="142" cy="145" r="134" fill="var(--white)"/>
    <circle cx="138" cy="145" r="128" fill="url(#repairTone)" role="img" aria-label="Photo of a technician repairing plumbing pipes"/>
  </svg>

  <svg class="photo-ring errand" width="300" height="280" viewBox="0 0 300 280">
    <defs>
      <linearGradient id="errandTone" x1="0" y1="0" x2="1" y2="1">
        <stop offset="0" stop-color="#d9d3c4"/>
        <stop offset="1" stop-color="var(--photo-warm)"/>
      </linearGradient>
    </defs>
    <circle cx="152" cy="138" r="134" fill="var(--red)"/>
    <circle cx="142" cy="138" r="126" fill="var(--white)"/>
    <circle cx="138" cy="138" r="120" fill="url(#errandTone)" role="img" aria-label="Photo of a shopper holding a grocery list over a cart"/>
  </svg>

  <div class="brand">
    <span class="mark"></span>
    <span class="name">Cedar Row Maintenance and Concierge</span>
  </div>

  <svg class="footer-wave" width="859" height="210" viewBox="0 0 859 210">
    <path d="M0 40 Q430 -20 859 40 L859 210 L0 210 Z" fill="var(--light-grey)"/>
    <path d="M0 52 Q430 -4 859 52 L859 210 L0 210 Z" fill="var(--red)"/>
  </svg>

  <p class="offer">We offer monthly service agreements and 24/7 access</p>
  <div class="divider"></div>
  <div class="contact">
    <p class="prompt">Call text or e-mail<br>for more information</p>
    <p class="phone">704.555.0187</p>
    <p class="email">1cedarrowmaint@quillpostmail.com</p>
  </div>
</main>
</body>
</html>
```